'Brantley Electrical' web design

I need a web design for an electrical/electrician company based in sydney called brantley electrical. The logo design and business card design have been uploaded to be used on the web design. I want the design to be very modern and clean. I want the sector designs on the business card, i.e "residential", "commercial" etc, to be fleshed out on the front page. Base those sector designs off the business card but try to make them more minimal and modern to suit the website. Contact details are also on the business card. Try to suit the colour scheme of the logo. The sector designs should be up the top and linked so when clicked it will scroll down the website to brief descriptions of the work the company does in those sectors. I want the website to mainly attract builders, insurance companies and the commercial sector. I want the website to look unique. Custom graphics would be nice to make the website standout. I don't want the website to look like generic.

Target Market(s)

Builders, commercial sector, home owners

Industry/Entity Type

Electrical/Construction

Coding

Coded - Design and coding required

Number of Pages Required

3 page

Requirements
Must have
• Modern design
Nice to have
• Custom graphics that make the website unique

```html
<!DOCTYPE html>
<html lang="en">
<head>
<meta charset="utf-8">
<title>Brantley Electrical — Powering Your Projects</title>
<link href="https://fonts.googleapis.com/css2?family=Montserrat:wght@400;500;600;700;800&display=swap" rel="stylesheet">
<style>
:root{
  --navy:#111a31;
  --navy-deep:#0c1327;
  --navy-mid:#1a2644;
  --navy-light:#22304f;
  --ring:#1c2741;
  --yellow:#ffd21a;
  --orange:#f08a24;
  --blue:#2f86e0;
  --white:#ffffff;
  --muted:#b9c2d6;
  --card:#e4e2f2;
}
*{margin:0;padding:0;box-sizing:border-box}
html,body{width:1200px;height:3499px;overflow:hidden}
body{position:relative;background:var(--navy);font-family:'Montserrat',sans-serif;color:var(--white)}
.abs{position:absolute}
.backdrop{position:absolute;left:0;top:0;width:1200px;height:3499px}
.top-rule{position:absolute;left:0;top:0;width:1200px;height:5px;background:var(--yellow)}
.header-line{position:absolute;left:0;top:90px;width:1200px;height:1px;background:#2c3956}
.brand{position:absolute;display:flex;align-items:center;gap:10px;font-weight:700;color:var(--white);letter-spacing:.5px}
.brand .dot{width:26px;height:26px;background:var(--orange);border-radius:50%}
.brand-tag{position:absolute;font-size:7px;letter-spacing:4px;color:var(--muted);font-weight:500}
.nav{position:absolute;top:52px;font-size:14px;color:#d7ddeb}
.nav.active{color:var(--yellow);font-weight:600}
.phone{position:absolute;left:722px;top:12px;display:flex;align-items:center;gap:10px;font-size:15px;font-weight:600}
.ring-ico{width:28px;height:28px;border:1.5px solid #cfd6e6;border-radius:50%;display:flex;align-items:center;justify-content:center}
.social-top{position:absolute;top:10px;width:27px;height:27px;border:1.5px solid #cfd6e6;border-radius:50%}
.social-top::after{content:"";position:absolute;left:9px;top:9px;width:6px;height:6px;background:#cfd6e6;border-radius:50%}
.eyebrow{position:absolute;color:var(--blue);font-size:15px;letter-spacing:1px;font-weight:500}
.hero-eyebrow{font-size:20px;letter-spacing:3px}
.hero-title{position:absolute;left:160px;top:272px;font-size:35px;line-height:44px;font-weight:700;letter-spacing:1px}
.hero-sub{position:absolute;left:160px;top:372px;font-size:20px;color:#d5dbe8;letter-spacing:.5px}
.btn{position:absolute;background:var(--yellow);color:#1b2030;border-radius:22px;font-size:15px;font-weight:500;display:flex;align-items:center;justify-content:center}
.photo{position:absolute;border-radius:50%}
.section-title{position:absolute;left:0;width:1200px;text-align:center;font-weight:700;font-size:28px}
.section-eyebrow{position:absolute;left:0;width:1200px;text-align:center;color:var(--blue);font-size:15px;letter-spacing:.5px}
.divider{position:absolute;left:560px;width:80px;height:20px}
.about-title{position:absolute;left:603px;top:826px;font-size:28px;font-weight:700;letter-spacing:.5px}
.about-text{position:absolute;left:603px;top:908px;width:440px;font-size:15px;line-height:28px;color:#cdd4e3}
.sector{position:absolute;width:210px;text-align:center}
.sector .num{position:absolute;left:0;top:-4px;font-size:58px;line-height:1;font-weight:800;color:#27334f}
.sector .outer{margin:0 auto;width:176px;height:176px;border-radius:50%;background:#18223d;display:flex;align-items:center;justify-content:center}
.sector .inner{width:136px;height:136px;border-radius:50%;background:#202c49;display:flex;align-items:center;justify-content:center}
.sector h3{margin-top:21px;color:var(--blue);font-size:17px;font-weight:700}
.sector p{margin-top:4px;font-size:13px;line-height:21px;color:#b7c0d3}
.tile{position:absolute;background:linear-gradient(135deg,#8b8f96,#3b3f46)}
.tile.feature{background:linear-gradient(180deg,#6d8fc0 0%,#3f78c8 70%,#2f70d2 100%)}
.tile-label{position:absolute;left:18px;bottom:57px;font-size:20px;font-weight:700}
.tile-link{position:absolute;left:18px;bottom:28px;font-size:15px;text-decoration:underline}
.glow{position:absolute;border-radius:50%;background:#1d3a78;opacity:.45;filter:blur(6px)}
.avatar{position:absolute;border-radius:50%;background:radial-gradient(circle at 50% 40%,#c99b7f,#6e4a3a);border:3px solid #f3f4f8}
.review{position:absolute;left:395px;top:2685px;width:399px;height:156px;background:var(--card);border-radius:6px;color:#3a3f55}
.review .quote{position:absolute;left:88px;top:20px;width:270px;font-size:12.5px;line-height:21px}
.review .name{position:absolute;left:61px;top:110px;font-size:12px;font-weight:700;color:#1e2540}
.review .role{position:absolute;left:61px;top:127px;font-size:12px}
.review .mark{position:absolute;font-size:80px;font-weight:800;color:#fff;line-height:1}
.footer{position:absolute;left:0;top:3106px;width:1200px;height:393px;background:var(--navy-mid);border-radius:70px 70px 0 0}
.f-head{position:absolute;font-size:16px;font-weight:600}
.f-head::after{content:"";position:absolute;left:0;top:26px;width:38px;height:2px;background:var(--yellow)}
.f-text{position:absolute;font-size:13px;line-height:21px;color:#d3d9e6}
.f-label{font-weight:600;font-size:14px;color:#fff}
.f-ico{position:absolute;width:36px;height:36px;border:1.5px solid #cfd6e6;border-radius:50%;display:flex;align-items:center;justify-content:center}
.q-link{position:absolute;left:748px;font-size:13.5px;color:#d3d9e6}
.q-link::before{content:"";position:absolute;left:-15px;top:7px;width:5px;height:5px;border-radius:50%;background:var(--blue)}
.q-link.active{color:var(--yellow);font-weight:600}
.s-ico{position:absolute;left:903px;width:23px;height:23px;border:1.5px solid #cfd6e6;border-radius:50%}
.s-link{position:absolute;left:937px;font-size:13.5px;color:#d3d9e6}
.copyright{position:absolute;left:0;top:3462px;width:1200px;text-align:center;font-size:15px;color:#e2e6ef}
</style>
</head>
<body>

<svg class="backdrop" viewBox="0 0 1200 3499" aria-hidden="true">
  <defs>
    <linearGradient id="heroBg" x1="0" y1="0" x2="1" y2="1">
      <stop offset="0" stop-color="#1b2a4c"/><stop offset="1" stop-color="#101932"/>
    </linearGradient>
    <linearGradient id="bandBg" x1="0" y1="0" x2="1" y2="0">
      <stop offset="0" stop-color="#0f1830"/><stop offset="1" stop-color="#1f3258"/>
    </linearGradient>
    <radialGradient id="revBg" cx=".5" cy=".5" r=".6">
      <stop offset="0" stop-color="#172649"/><stop offset="1" stop-color="#0d152b"/>
    </radialGradient>
  </defs>
  <rect width="1200" height="3499" fill="#111a31"/>
  <path d="M0 0H1200V560L0 560Z" fill="url(#heroBg)"/>
  <path d="M0 430 L700 300 L1200 420 V1120 L0 1380Z" fill="#0e1629"/>
  <path d="M0 1380 L1200 1080 V1260 L0 1500Z" fill="url(#bandBg)" opacity=".7"/>
  <rect x="0" y="1500" width="1200" height="900" fill="#101a33"/>
  <rect x="0" y="2350" width="1200" height="800" fill="url(#revBg)"/>
  <path d="M660 200 A292 292 0 0 1 1200 120 V640 Q1180 720 1080 715 L900 715 A292 292 0 0 1 660 200Z" fill="#1a2542"/>
  <circle cx="303" cy="929" r="292" fill="#161f39"/>
</svg>

<div class="top-rule"></div>
<div class="brand" style="left:163px;top:42px;font-size:22px"><span class="dot"></span>BRANTLEY ELECTRICAL</div>
<div class="brand-tag" style="left:200px;top:70px">POWERING YOUR PROJECTS</div>

<div class="phone"><span class="ring-ico"><svg width="14" height="14" viewBox="0 0 24 24"><path d="M6 2l4 4-2 3a13 13 0 0 0 7 7l3-2 4 4-3 4C10 22 2 14 2 5z" fill="#fff"/></svg></span>1800 555 0142</div>
<span class="social-top" style="left:899px"></span>
<span class="social-top" style="left:937px"></span>
<span class="social-top" style="left:975px"></span>
<span class="social-top" style="left:1013px"></span>

<span class="nav active" style="left:541px">Home</span>
<span class="nav" style="left:608px">About</span>
<span class="nav" style="left:676px;top:50px">Projects</span>
<span class="nav" style="left:760px">Innovation</span>
<span class="nav" style="left:864px;top:50px">Clients Gallery</span>
<span class="nav" style="left:989px">Career</span>
<svg class="abs" style="left:556px;top:71px" width="8" height="12" viewBox="0 0 8 12"><path d="M5 0L0 7h3l-1 5 6-8H5z" fill="var(--yellow)"/></svg>
<div class="header-line"></div>

<!-- Hero -->
<div class="eyebrow hero-eyebrow" style="left:162px;top:236px">WE ARE THE</div>
<h1 class="hero-title">BRANTLEY ELECTRICAL<br>POWERING YOUR PROJECTS</h1>
<p class="hero-sub">Voice of the Electrical Construction Industry</p>
<div class="btn" style="left:170px;top:421px;width:131px;height:43px">Read More</div>
<svg class="abs" style="left:592px;top:462px" width="16" height="78" viewBox="0 0 16 78"><line x1="8" y1="0" x2="8" y2="50" stroke="#2d3a58"/><rect x="3" y="55" width="10" height="20" rx="5" fill="none" stroke="var(--blue)" stroke-width="2"/><line x1="8" y1="60" x2="8" y2="65" stroke="var(--blue)" stroke-width="2"/></svg>
<div class="photo" role="img" aria-label="Two electricians in hard hats and hi-vis vests testing a switchboard with a multimeter" style="left:729px;top:139px;width:388px;height:388px;background:radial-gradient(circle at 30% 30%,#f2c879,#8a6a3e 45%,#2c3650 90%)"></div>

<!-- About -->
<div class="photo" role="img" aria-label="Electrician in orange vest and yellow hard hat using a radio beneath a steel transmission tower" style="left:76px;top:702px;width:454px;height:454px;border:2px solid var(--yellow);background:radial-gradient(circle at 65% 55%,#d8693a,#9b7660 35%,#dfe4ec 70%)"></div>
<div class="eyebrow" style="left:603px;top:798px">INFORMATION</div>
<h2 class="about-title">ABOUT THE COMPANY</h2>
<svg class="abs" style="left:603px;top:873px" width="56" height="20" viewBox="0 0 56 20"><path d="M9 0L1 11h6l-2 9 10-13H9z" fill="var(--yellow)"/><line x1="24" y1="10" x2="56" y2="10" stroke="#c5ccdb" stroke-width="1.5"/></svg>
<p class="about-text">Lorem ipsum dolor sit amet, consectetuer adipiscing elit, sed diam nonummy nibh euismod tincidunt ut laoreet dolore magna aliquam erat volutpat. Ut wisi enim ad minim veniam, quis nostrud exerci tation...</p>
<div class="btn" style="left:603px;top:1043px;width:121px;height:38px">Read More</div>

<!-- What we do -->
<div class="section-eyebrow" style="top:1326px">MY WORKS</div>
<h2 class="section-title" style="top:1352px">WHAT WE DO?</h2>
<svg class="divider" style="top:1393px" viewBox="0 0 80 20"><line x1="0" y1="10" x2="26" y2="10" stroke="#c5ccdb" stroke-width="1.5"/><path d="M43 1L35 12h6l-2 8 10-12h-6z" fill="var(--yellow)"/><line x1="54" y1="10" x2="80" y2="10" stroke="#c5ccdb" stroke-width="1.5"/></svg>

<div class="sector" style="left:157px;top:1412px"><span class="num">01</span><div class="outer"><div class="inner">
  <svg width="54" height="50" viewBox="0 0 54 50"><rect x="10" y="4" width="22" height="46" fill="#fff"/><rect x="32" y="18" width="14" height="32" fill="#fff"/><g fill="#202c49"><rect x="14" y="10" width="4" height="4"/><rect x="24" y="10" width="4" height="4"/><rect x="14" y="20" width="4" height="4"/><rect x="24" y="20" width="4" height="4"/><rect x="14" y="30" width="4" height="4"/><rect x="24" y="30" width="4" height="4"/><rect x="36" y="24" width="4" height="4"/><rect x="36" y="34" width="4" height="4"/><rect x="18" y="40" width="6" height="10"/></g></svg>
</div></div><h3>Commercial</h3><p>Lorem ipsum dolor sit amet,<br>consectetuer adipisci...</p></div>

<div class="sector" style="left:382px;top:1412px"><span class="num" style="top:2px">02</span><div class="outer"><div class="inner">
  <svg width="54" height="50" viewBox="0 0 54 50"><rect x="6" y="4" width="42" height="5" fill="#fff"/><rect x="10" y="9" width="5" height="41" fill="#fff"/><line x1="40" y1="9" x2="40" y2="22" stroke="#fff" stroke-width="2"/><rect x="22" y="28" width="28" height="22" fill="#fff"/><rect x="30" y="38" width="8" height="12" fill="#202c49"/></svg>
</div></div><h3>Construction</h3><p>Lorem ipsum dolor sit amet,<br>consectetuer adipisci...</p></div>

<div class="sector" style="left:607px;top:1412px"><span class="num" style="top:2px">03</span><div class="outer"><div class="inner">
  <svg width="54" height="50" viewBox="0 0 54 50"><rect x="14" y="4" width="7" height="22" fill="#fff"/><rect x="4" y="24" width="46" height="26" fill="#fff"/><rect x="34" y="14" width="14" height="10" fill="#fff"/><g fill="#202c49"><rect x="10" y="32" width="30" height="4"/><rect x="10" y="40" width="8" height="10"/></g></svg>
</div></div><h3>Industrial</h3><p>Lorem ipsum dolor sit amet,<br>consectetuer adipisci...</p></div>

<div class="sector" style="left:832px;top:1412px"><span class="num" style="top:2px;left:-3px">04</span><div class="outer"><div class="inner">
  <svg width="58" height="40" viewBox="0 0 58 40"><path d="M2 20L16 6l14 14v18H2z" fill="#fff"/><path d="M28 20L42 6l14 14v18H28z" fill="#fff"/><rect x="11" y="26" width="8" height="12" fill="#202c49"/><rect x="38" y="26" width="8" height="12" fill="#202c49"/></svg>
</div></div><h3>Residential</h3><p>Lorem ipsum dolor sit amet,<br>consectetuer adipisci...</p></div>

<div class="btn" style="left:539px;top:1690px;width:122px;height:41px">Contact Us</div>

<!-- Work gallery -->
<div class="section-eyebrow" style="top:1805px">MY WORKS</div>
<h2 class="section-title" style="top:1832px">Work Gallery</h2>
<svg class="divider" style="top:1872px" viewBox="0 0 80 20"><line x1="0" y1="10" x2="26" y2="10" stroke="#c5ccdb" stroke-width="1.5"/><path d="M43 1L35 12h6l-2 8 10-12h-6z" fill="var(--yellow)"/><line x1="54" y1="10" x2="80" y2="10" stroke="#c5ccdb" stroke-width="1.5"/></svg>

<div class="tile" role="img" aria-label="Black and white photo of an electrician working on a switchboard" style="left:0;top:1956px;width:217px;height:313px"></div>
<div class="tile" role="img" aria-label="Black and white photo of hands wiring a wall outlet" style="left:244px;top:1932px;width:219px;height:175px"></div>
<div class="tile" role="img" aria-label="Silhouette of workers on scaffolding at a building site" style="left:244px;top:2133px;width:219px;height:176px;background:linear-gradient(180deg,#d9d9d9,#2a2a2a)"></div>
<div class="tile feature" role="img" aria-label="Two engineers in hard hats reviewing plans at a construction site" style="left:490px;top:1956px;width:219px;height:313px">
  <span class="tile-label">Construction</span><span class="tile-link">Read More</span>
</div>
<div class="tile" role="img" aria-label="Black and white photo of an industrial machinery hall" style="left:736px;top:1932px;width:218px;height:175px;background:linear-gradient(135deg,#d0d0d0,#555)"></div>
<div class="tile" role="img" aria-label="Black and white photo of an electrician fitting cable to a brick wall" style="left:736px;top:2133px;width:218px;height:176px"></div>
<div class="tile" role="img" aria-label="Black and white photo of an electrician with a screwdriver at a panel" style="left:981px;top:1956px;width:219px;height:313px"></div>

<!-- Reviews -->
<div class="glow" style="left:330px;top:2510px;width:80px;height:80px"></div>
<div class="glow" style="left:760px;top:2530px;width:60px;height:60px"></div>
<div class="glow" style="left:230px;top:2730px;width:60px;height:60px"></div>
<div class="glow" style="left:850px;top:2760px;width:50px;height:50px"></div>
<div class="glow" style="left:900px;top:2850px;width:40px;height:40px"></div>

<div class="section-eyebrow" style="top:2398px">TESTIMONIALS</div>
<h2 class="section-title" style="top:2424px">Customer Reviews</h2>
<svg class="abs" style="left:545px;top:2472px" width="110" height="24" viewBox="0 0 110 24"><line x1="0" y1="12" x2="35" y2="12" stroke="#c5ccdb" stroke-width="1.5"/><path d="M58 1L47 15h8l-3 9 12-15h-8z" fill="var(--yellow)"/><line x1="75" y1="12" x2="110" y2="12" stroke="#c5ccdb" stroke-width="1.5"/></svg>

<div class="avatar" role="img" aria-label="Customer portrait" style="left:471px;top:2531px;width:98px;height:98px"></div>
<div class="avatar" role="img" aria-label="Customer portrait" style="left:273px;top:2591px;width:60px;height:60px"></div>
<div class="avatar" role="img" aria-label="Customer portrait" style="left:683px;top:2630px;width:90px;height:90px;border:none;background:#c8713a"></div>
<div class="avatar" role="img" aria-label="Customer portrait" style="left:906px;top:2649px;width:60px;height:60px"></div>
<div class="review">
  <span class="mark" style="left:10px;top:-2px">“</span>
  <p class="quote">“ Lorem ipsum dolor sit amet, consectetuer adipiscing elit, sed diam nonummy nibh euismod tincidunt ut laoreet dolore magna aliqu... ”</p>
  <span class="name">MARA QUILLEN</span>
  <span class="role">sit amet,</span>
  <span class="mark" style="right:12px;top:92px">”</span>
</div>
<div class="avatar" role="img" aria-label="Featured reviewer portrait" style="left:343px;top:2718px;width:104px;height:104px;border-width:4px;background:radial-gradient(circle,#e8b9a2,#d36b6b)"></div>
<div class="avatar" role="img" aria-label="Customer portrait" style="left:270px;top:2828px;width:74px;height:74px"></div>
<div class="avatar" role="img" aria-label="Customer portrait" style="left:497px;top:2898px;width:44px;height:44px"></div>
<div class="avatar" role="img" aria-label="Customer portrait" style="left:793px;top:2871px;width:60px;height:60px;border:none;background:radial-gradient(circle at 50% 40%,#c99b7f,#2f6fc0)"></div>

<div class="btn" style="left:539px;top:2982px;width:122px;height:40px">View All</div>

<!-- Footer -->
<footer class="footer"></footer>
<div class="brand" style="left:163px;top:3206px;font-size:18px"><span class="dot" style="width:20px;height:20px"></span>BRANTLEY ELECTRICAL</div>
<p class="f-text" style="left:165px;top:3254px;width:240px;font-size:12.5px">“ Lorem ipsum dolor sit amet, onsectetuer adipiscing elit, sed diam nonummy nibh euismod tincidunt ut laoreet dolore magna aliqu... ”</p>

<div class="f-head" style="left:456px;top:3164px">Contact Details</div>
<span class="f-ico" style="left:453px;top:3221px"><svg width="14" height="18" viewBox="0 0 14 18"><path d="M7 0a7 7 0 0 1 7 7c0 5-7 11-7 11S0 12 0 7a7 7 0 0 1 7-7z" fill="#fff"/><circle cx="7" cy="7" r="2.5" fill="var(--navy-mid)"/></svg></span>
<div class="f-text" style="left:497px;top:3215px;line-height:19px"><span class="f-label">Address</span><br>48 Harbour Lane,<br>Sydney NSW 2000</div>
<span class="f-ico" style="left:453px;top:3290px"><svg width="14" height="14" viewBox="0 0 24 24"><path d="M6 2l4 4-2 3a13 13 0 0 0 7 7l3-2 4 4-3 4C10 22 2 14 2 5z" fill="#fff"/></svg></span>
<div class="f-text" style="left:497px;top:3287px;line-height:20px"><span class="f-label">Call Us</span><br><span style="font-size:15px">02 5550 1234</span></div>
<span class="f-ico" style="left:453px;top:3362px"><svg width="16" height="12" viewBox="0 0 16 12"><rect width="16" height="12" rx="1" fill="#fff"/><path d="M0 1l8 6 8-6" fill="none" stroke="var(--navy-mid)" stroke-width="1.5"/></svg></span>
<div class="f-text" style="left:497px;top:3359px;line-height:19px"><span class="f-label">Email Us</span><br><span style="font-size:11.5px">info@brantleyelectrical.com.au</span></div>

<div class="f-head" style="left:728px;top:3164px">Quick Links</div>
<span class="q-link active" style="top:3217px">Home</span>
<span class="q-link" style="top:3251px">About</span>
<span class="q-link" style="top:3285px">Projects</span>
<span class="q-link" style="top:3318px">Innovation</span>
<span class="q-link" style="top:3350px">Clients Gallery</span>
<span class="q-link" style="top:3384px">Career</span>

<div class="f-head" style="left:900px;top:3164px">Social Media</div>
<span class="s-ico" style="top:3214px"></span><span class="s-link" style="top:3216px">Facelink</span>
<span class="s-ico" style="top:3254px"></span><span class="s-link" style="top:3256px">Chirper</span>
<span class="s-ico" style="top:3298px"></span><span class="s-link" style="top:3300px">WorkNet</span>
<span class="s-ico" style="top:3339px"></span><span class="s-link" style="top:3341px">snapgram</span>

<p class="copyright">Copyright © 2023 Brantley Electrical Construction. All rights reserved.</p>

</body>
</html>
```